Business Card & Stationary
for Dental office
Professional
Ritika Dhulekar, DDS
18467 E Larchmont Rd
Wayne, MI 48184
toothclinic@mailbrook.com
PineLedgeDental.com
Logo has business name.
Back of business card will be used for pre-printed appointment information.
Business logo on Gray color
Business Logo
Sample back of card

```html
<!DOCTYPE html>
<html lang="en">
<head>
<meta charset="utf-8">
<title>PineLedge Dental Stationery</title>
<link href="https://fonts.googleapis.com/css2?family=Lato:wght@400;700&display=swap" rel="stylesheet">
<style>
  :root {
    --backdrop: #e9dcc6;
    --paper: #ffffff;
    --navy: #1f3f9e;
    --royal: #2f5fc8;
    --sky: #3fa9e6;
    --ice: #d9eefa;
    --ink: #3a4a66;
    --label: #7a6a55;
  }
  * { box-sizing: border-box; margin: 0; padding: 0; }
  html, body { width: 1200px; height: 446px; overflow: hidden; }
  body {
    background: var(--backdrop);
    font-family: "Lato", Arial, sans-serif;
    color: var(--ink);
    position: relative;
  }
  .piece { position: absolute; background: var(--paper); box-shadow: 0 1px 4px rgba(60,40,20,.25); overflow: hidden; }
  .piece svg.curve { position: absolute; inset: 0; width: 100%; height: 100%; }
  .label { position: absolute; font-size: 5px; letter-spacing: .5px; text-transform: uppercase; color: var(--label); white-space: nowrap; }
  .brand { position: absolute; display: flex; align-items: center; gap: 4px; color: var(--royal); font-weight: 700; white-space: nowrap; }
  .brand .dot { border-radius: 50%; background: var(--sky); flex: none; }
  .contact { position: absolute; font-size: 5px; line-height: 8px; color: var(--ink); list-style: none; white-space: nowrap; }
  .contact li { display: flex; align-items: center; gap: 3px; }
  .contact li::before { content: ""; width: 4px; height: 4px; border-radius: 50%; background: var(--royal); }
  .footer-line { position: absolute; bottom: 12px; left: 40px; right: 14px; display: flex; justify-content: space-between; font-size: 4.5px; color: var(--ink); white-space: nowrap; }
  .footer-line span::before { content: ""; display: inline-block; width: 3px; height: 3px; margin-right: 2px; border-radius: 50%; background: var(--royal); }

  /* business cards */
  .card { left: 8px; width: 62px; height: 34px; }
  .card-front { top: 88px; background: var(--navy); }
  .card-front .face { position: absolute; left: 14px; top: 2px; right: 2px; bottom: 2px; background: var(--paper); border-radius: 0 0 0 18px / 0 0 0 30px; }
  .card-front .brand { left: 18px; top: 5px; font-size: 4.6px; gap: 2px; }
  .card-front .brand .dot { width: 4px; height: 4px; }
  .card-front .details { position: absolute; left: 20px; top: 12px; font-size: 2.6px; line-height: 3.6px; white-space: nowrap; }
  .card-back { top: 143px; }
  .card-back .title { position: absolute; left: 12px; top: 6px; font-size: 3.4px; font-weight: 700; color: var(--royal); white-space: nowrap; }
  .card-back .field { position: absolute; left: 12px; right: 6px; font-size: 2.8px; border-bottom: .4px solid #9aa8c0; }

  /* letterheads */
  .letterhead { top: 12px; width: 288px; height: 413px; }
  .letterhead-one { left: 175px; }
  .letterhead-two { left: 480px; }
  .letterhead .brand { top: 16px; font-size: 9px; }
  .letterhead .brand .dot { width: 7px; height: 7px; }
  .letterhead-one .brand { left: 104px; }
  .letterhead-one .contact { left: 200px; top: 12px; }
  .letterhead-two .brand { left: 108px; }

  /* envelopes */
  .envelope { left: 840px; width: 350px; }
  .envelope-back { top: 12px; height: 140px; background: linear-gradient(180deg, var(--navy), var(--royal)); }
  .envelope-flap { position: absolute; left: 840px; width: 350px; }
  .envelope-open { top: 112px; height: 92px; background: var(--sky); }
  .envelope-inner { top: 196px; height: 92px; background: var(--paper); box-shadow: 0 1px 4px rgba(60,40,20,.25); }
  .envelope-front { top: 300px; height: 128px; }
  .envelope-front .brand { left: 40px; top: 14px; font-size: 8px; }
  .envelope-front .brand .dot { width: 7px; height: 7px; }
</style>
</head>
<body>

  <p class="label" style="left:8px;top:78px">Business card front</p>
  <div class="piece card card-front">
    <div class="face"></div>
    <div class="brand"><span class="dot"></span>PineLedge Dental</div>
    <div class="details">
      <div>Ritika Dhulekar, DDS</div>
      <div>18467 E Larchmont Rd</div>
      <div>Wayne, MI 48184</div>
      <div>toothclinic@mailbrook.com</div>
      <div>PineLedgeDental.com</div>
    </div>
  </div>

  <p class="label" style="left:8px;top:133px">Appointment card back</p>
  <div class="piece card card-back">
    <svg class="curve" viewBox="0 0 62 34" preserveAspectRatio="none" aria-hidden="true">
      <path d="M0 0 H7 C4 12 4 24 9 34 H0 Z" fill="var(--navy)"/>
      <path d="M7 0 C4 12 4 24 9 34" fill="none" stroke="var(--sky)" stroke-width="1"/>
    </svg>
    <p class="title">Your next appointment</p>
    <p class="field" style="top:14px">Date</p>
    <p class="field" style="top:22px">Time</p>
  </div>
  <p class="label" style="left:8px;top:186px">Business card back</p>

  <div class="piece letterhead letterhead-one">
    <svg class="curve" viewBox="0 0 288 413" preserveAspectRatio="none" aria-hidden="true">
      <path d="M0 0 H22 C8 140 8 280 44 413 H0 Z" fill="var(--navy)"/>
      <path d="M0 0 H12 C2 140 2 280 26 413 H0 Z" fill="var(--royal)"/>
      <path d="M22 0 C8 140 8 280 44 413" fill="none" stroke="var(--sky)" stroke-width="3"/>
    </svg>
    <div class="brand"><span class="dot"></span>PineLedge Dental</div>
    <ul class="contact">
      <li>18467 E Larchmont Rd</li>
      <li>Wayne, MI 48184</li>
      <li>toothclinic@mailbrook.com</li>
      <li>PineLedgeDental.com</li>
    </ul>
  </div>
  <p class="label" style="left:285px;top:432px">Letterhead Design Option 1</p>

  <div class="piece letterhead letterhead-two">
    <svg class="curve" viewBox="0 0 288 413" preserveAspectRatio="none" aria-hidden="true">
      <path d="M0 0 H22 C8 140 8 280 44 413 H0 Z" fill="var(--navy)"/>
      <path d="M0 0 H12 C2 140 2 280 26 413 H0 Z" fill="var(--royal)"/>
      <path d="M22 0 C8 140 8 280 44 413" fill="none" stroke="var(--sky)" stroke-width="3"/>
    </svg>
    <div class="brand"><span class="dot"></span>PineLedge Dental</div>
    <div class="footer-line">
      <span>18467 E Larchmont Rd, Wayne, MI 48184</span>
      <span>toothclinic@mailbrook.com</span>
      <span>PineLedgeDental.com</span>
    </div>
  </div>
  <p class="label" style="left:590px;top:432px">Letterhead Design Option 2</p>

  <div class="piece envelope envelope-back"></div>
  <div class="envelope-flap envelope-open"></div>
  <div class="envelope-flap envelope-inner">
    <svg viewBox="0 0 350 92" preserveAspectRatio="none" aria-hidden="true" style="position:absolute;inset:0;width:100%;height:100%">
      <path d="M0 0 L175 60 L350 0" fill="none" stroke="#dde3ec" stroke-width="1"/>
    </svg>
  </div>

  <div class="piece envelope envelope-front">
    <svg class="curve" viewBox="0 0 350 128" preserveAspectRatio="none" aria-hidden="true">
      <path d="M0 0 H14 C6 40 8 90 26 128 H0 Z" fill="var(--navy)"/>
      <path d="M14 0 C6 40 8 90 26 128" fill="none" stroke="var(--sky)" stroke-width="3"/>
    </svg>
    <div class="brand"><span class="dot"></span>PineLedge Dental</div>
  </div>
  <p class="label" style="left:975px;top:432px">Envelope Design Option</p>

</body>
</html>
```